stars + comments Reviews website design (similar to quarn concept)

Please refer to attached logo and wire frames
----------------------------------------------------------------------------------------------------
we are a company based in egypt, seeking a design for a website that allows user to find doctors using search and filters.
also it allows user to review this doctor through providing comment and 1 to 5 stars
i need 4 main pages designs:
1- Doctors list/favorites list
2- Doctor view
3- Add doctor (3 steps)
4- Sign-in/sign up
5- Menu design
am into the colors teal/turquoise (though am open for different opinion)
i don't want the design theme to be doctors specific
am into the school of very clean, very neat, very simple
(plombex, ruvanteo, melvoshade designs are appealing to me)

Number of Pages Required

4 page

Font styles to use
Sans Serif

Colors
00a990
33b8a4

Requirements
Must have
• website will be bilingual/ bi-directional (English and Arabic)
• designer needs to provide another copy of the design with "right to left" orientation
• interactive button animation

```html
<!DOCTYPE html>
<html lang="en">
<head>
<meta charset="utf-8">
<title>Clinora – Doctors</title>
<link href="https://fonts.googleapis.com/css2?family=Roboto:wght@300;400;500;700&display=swap" rel="stylesheet">
<style>
:root{
  --teal:#00a990;
  --teal-light:#33b8a4;
  --page:#fafafa;
  --white:#fff;
  --border:#e6e6e6;
  --text:#3c3c3c;
  --muted:#8a8a8a;
  --select-btn:#c4ccca;
  --star:#f5a800;
  --ribbon:#f0f0f0;
}
*{box-sizing:border-box;margin:0;padding:0}
html,body{width:1200px;height:1054px;overflow:hidden}
body{font-family:'Roboto',sans-serif;background:var(--page);color:var(--text);position:relative}

.site-header{height:78px;background:var(--teal);display:flex;align-items:center;padding:0 60px;justify-content:space-between}
.brand{display:flex;align-items:center;gap:8px;color:var(--white);font-size:36px;font-weight:500;letter-spacing:.5px}
.brand-dot{width:22px;height:22px;border-radius:50%;background:var(--white)}
.main-nav{display:flex;align-items:center;height:100%}
.nav-item{display:flex;align-items:center;gap:6px;color:var(--white);font-size:14px;padding:0 18px;border-right:1px solid rgba(255,255,255,.3);line-height:24px}
.nav-item:last-of-type{border-right:none}
.nav-item svg{width:18px;height:18px;stroke:var(--white);fill:none;stroke-width:1.5}
.caret{width:0;height:0;border-left:5px solid transparent;border-right:5px solid transparent;border-top:6px solid var(--white);margin-left:4px}
.user-menu{display:flex;align-items:center;gap:6px;padding-left:18px;border-left:1px solid rgba(255,255,255,.3)}
.avatar{width:42px;height:42px;border-radius:50%;border:2px solid var(--white);background:linear-gradient(135deg,#c79a7a,#6e4a38)}
.user-name{color:var(--white);font-size:14px;line-height:16px}
.user-name small{display:block;font-size:10px}

.filters{background:var(--white);height:85px;display:flex;align-items:center;padding-left:134px;gap:9px}
.select{display:flex;width:159px;height:30px;border:1px solid var(--border)}
.select span{flex:1;font-size:13px;color:var(--muted);padding:7px 8px}
.select i{width:33px;background:var(--select-btn);display:flex;align-items:center;justify-content:center}
.search{display:flex;width:231px;height:30px;border:1px solid var(--border)}
.search span{flex:1;font-size:13px;color:var(--muted);padding:7px 8px}
.search i{width:42px;background:var(--teal);display:flex;align-items:center;justify-content:center}

.listing{padding:18px 60px 0}
.section-title{display:flex;align-items:center;gap:8px;height:46px}
.title-icon{width:44px;height:44px;border-radius:50%;border:2px solid var(--teal);display:flex;align-items:center;justify-content:center}
.section-title h1{font-size:19px;font-weight:400;color:var(--teal)}
.section-title h1 span{font-size:14px;color:var(--text)}
.section-title hr{flex:1;border:none;border-top:1px solid var(--border);margin-left:22px}

.doctor-list{margin-top:20px;display:flex;flex-direction:column;gap:19px}
.doctor-card{position:relative;height:126px;background:var(--white);border:1px solid var(--border);display:flex;align-items:center;padding-left:21px}
.doctor-photo{width:90px;height:84px}
.doctor-info{margin-left:21px}
.doctor-name{font-size:19px;color:var(--teal)}
.doctor-name small{font-size:14px}
.doctor-spec{font-size:17px;margin-top:6px;color:var(--text)}
.doctor-address{font-size:12px;margin-top:6px;color:var(--text)}
.rating{position:absolute;right:0;top:41px;width:168px;height:41px;background:var(--ribbon);clip-path:polygon(8px 0,100% 0,100% 100%,0 100%,8px 50%,0 0);display:flex;align-items:center;justify-content:flex-end;padding-right:18px;gap:6px}
.stars{display:flex}
.stars svg{width:17px;height:17px}
.rating span{font-size:12px;color:var(--muted)}
.fav{position:absolute;right:18px;top:91px;width:20px;height:18px}

.loader{position:absolute;left:545px;top:840px;width:110px;height:110px}

.site-footer{position:absolute;bottom:0;left:0;width:1200px;height:68px;background:var(--white);display:flex;align-items:center;justify-content:space-between;padding:0 60px}
.site-footer p{font-size:13px;color:var(--text)}
.social{display:flex;gap:14px}
.social a{display:flex;align-items:center;gap:4px;font-size:11px;color:var(--muted);text-decoration:none}
.social a i{width:14px;height:14px;border-radius:50%;border:1px solid var(--muted)}
</style>
</head>
<body>
<svg width="0" height="0" style="position:absolute">
  <defs>
    <path id="star" d="M10 1l2.6 5.6 6.1.7-4.5 4.2 1.2 6L10 14.6 4.6 17.5l1.2-6L1.3 7.3l6.1-.7z"/>
    <linearGradient id="half"><stop offset="50%" stop-color="#f5a800"/><stop offset="50%" stop-color="#fff"/></linearGradient>
    <path id="heart" d="M10 17s-8-4.8-8-10a4 4 0 0 1 8-1 4 4 0 0 1 8 1c0 5.2-8 10-8 10z"/>
  </defs>
</svg>

<header class="site-header">
  <div class="brand"><i class="brand-dot"></i>Clinora</div>
  <nav class="main-nav">
    <a class="nav-item"><svg viewBox="0 0 20 20"><path d="M2 10L10 3l8 7M5 8v9h10V8"/></svg>Home</a>
    <a class="nav-item"><svg viewBox="0 0 20 20"><use href="#heart"/></svg>Favorites</a>
    <a class="nav-item"><svg viewBox="0 0 20 20"><circle cx="9" cy="6" r="3.5"/><path d="M2 18c0-4 3-6 7-6M14 12v6M11 15h6"/></svg>Add Doctor</a>
    <a class="nav-item"><svg viewBox="0 0 20 20"><circle cx="10" cy="10" r="3"/><circle cx="10" cy="10" r="7.5" stroke-dasharray="3 2"/></svg>Settings<i class="caret"></i></a>
    <a class="nav-item"><svg viewBox="0 0 20 20"><rect x="2" y="4" width="16" height="12"/><path d="M2 4l8 7 8-7"/></svg>Contact Us</a>
    <div class="user-menu">
      <div class="avatar" role="img" aria-label="User profile photo"></div>
      <div class="user-name">Karim Toller<small>Sign out</small></div>
      <i class="caret"></i>
    </div>
  </nav>
</header>

<section class="filters">
  <div class="select"><span>Specialization</span><i><svg width="14" height="8" viewBox="0 0 14 8"><path d="M1 1l6 6 6-6" stroke="#fff" stroke-width="2" fill="none"/></svg></i></div>
  <div class="select"><span>Sub-specialization</span><i><svg width="14" height="8" viewBox="0 0 14 8"><path d="M1 1l6 6 6-6" stroke="#fff" stroke-width="2" fill="none"/></svg></i></div>
  <div class="select" style="width:132px"><span>Area</span><i><svg width="14" height="8" viewBox="0 0 14 8"><path d="M1 1l6 6 6-6" stroke="#fff" stroke-width="2" fill="none"/></svg></i></div>
  <div class="select" style="width:132px"><span>Gander</span><i><svg width="14" height="8" viewBox="0 0 14 8"><path d="M1 1l6 6 6-6" stroke="#fff" stroke-width="2" fill="none"/></svg></i></div>
  <div class="select" style="width:132px"><span>Rating</span><i><svg width="14" height="8" viewBox="0 0 14 8"><path d="M1 1l6 6 6-6" stroke="#fff" stroke-width="2" fill="none"/></svg></i></div>
  <div class="search"><span>Search</span><i><svg width="22" height="18" viewBox="0 0 22 18"><circle cx="8" cy="8" r="6" stroke="#fff" stroke-width="3" fill="none"/><path d="M12.5 12l7 5" stroke="#fff" stroke-width="3.5"/></svg></i></div>
</section>

<main class="listing">
  <div class="section-title">
    <div class="title-icon"><svg width="24" height="24" viewBox="0 0 24 24" fill="none" stroke="#3c3c3c" stroke-width="1.6"><path d="M5 3v6a4 4 0 0 0 8 0V3M9 13v3a4 4 0 0 0 8 0v-2"/><circle cx="17" cy="12" r="2"/></svg></div>
    <h1>Doctors <span>(15,123)</span></h1>
    <hr>
  </div>

  <div class="doctor-list">
    <article class="doctor-card">
      <div class="doctor-photo" role="img" aria-label="Portrait photo of the doctor" style="background:linear-gradient(160deg,#e9e9e9,#b89a86)"></div>
      <div class="doctor-info"><h2 class="doctor-name">Salma Rafeh <small>(1km away)</small></h2><p class="doctor-spec">Anesthesiologist</p><p class="doctor-address">73 Palm Lane, Westgate</p></div>
      <div class="rating"><div class="stars"><svg viewBox="0 0 20 20"><use href="#star" fill="#f5a800"/></svg><svg viewBox="0 0 20 20"><use href="#star" fill="#f5a800"/></svg><svg viewBox="0 0 20 20"><use href="#star" fill="#f5a800"/></svg><svg viewBox="0 0 20 20"><use href="#star" fill="#f5a800"/></svg><svg viewBox="0 0 20 20"><use href="#star" fill="url(#half)" stroke="#f5a800" stroke-width="1.3"/></svg></div><span>(123)</span></div>
      <svg class="fav" viewBox="0 0 20 19"><use href="#heart" fill="none" stroke="#555" stroke-width="1.6"/></svg>
    </article>
    <article class="doctor-card">
      <div class="doctor-photo" role="img" aria-label="Portrait photo of the doctor" style="background:linear-gradient(160deg,#d8d8d8,#7a5a48)"></div>
      <div class="doctor-info"><h2 class="doctor-name">Omar Zayed <small>(9kms away)</small></h2><p class="doctor-spec">Dentist</p><p class="doctor-address">48 Cedar Street, Eastfield</p></div>
      <div class="rating"><div class="stars"><svg viewBox="0 0 20 20"><use href="#star" fill="#f5a800"/></svg><svg viewBox="0 0 20 20"><use href="#star" fill="#f5a800"/></svg><svg viewBox="0 0 20 20"><use href="#star" fill="#f5a800"/></svg><svg viewBox="0 0 20 20"><use href="#star" fill="#f5a800"/></svg><svg viewBox="0 0 20 20"><use href="#star" fill="url(#half)" stroke="#f5a800" stroke-width="1.3"/></svg></div><span>(123)</span></div>
      <svg class="fav" viewBox="0 0 20 19"><use href="#heart" fill="#f5a800"/></svg>
    </article>
    <article class="doctor-card">
      <div class="doctor-photo" role="img" aria-label="Portrait photo of the doctor" style="background:linear-gradient(160deg,#f0e8e2,#c9663a)"></div>
      <div class="doctor-info"><h2 class="doctor-name">Dalia Fouad <small>(8kms away)</small></h2><p class="doctor-spec">Pediatrician</p><p class="doctor-address">122 Olive Street, Westgate</p></div>
      <div class="rating"><div class="stars"><svg viewBox="0 0 20 20"><use href="#star" fill="#f5a800"/></svg><svg viewBox="0 0 20 20"><use href="#star" fill="#f5a800"/></svg><svg viewBox="0 0 20 20"><use href="#star" fill="#f5a800"/></svg><svg viewBox="0 0 20 20"><use href="#star" fill="#f5a800"/></svg><svg viewBox="0 0 20 20"><use href="#star" fill="url(#half)" stroke="#f5a800" stroke-width="1.3"/></svg></div><span>(123)</span></div>
      <svg class="fav" viewBox="0 0 20 19"><use href="#heart" fill="none" stroke="#555" stroke-width="1.6"/></svg>
    </article>
    <article class="doctor-card">
      <div class="doctor-photo" role="img" aria-label="Portrait photo of the doctor" style="background:linear-gradient(160deg,#c9c9c9,#8a6a55)"></div>
      <div class="doctor-info"><h2 class="doctor-name">Salma Rafeh <small>(1km away)</small></h2><p class="doctor-spec">Anesthesiologist</p><p class="doctor-address">48 Olive Street, Westgate</p></div>
      <div class="rating"><div class="stars"><svg viewBox="0 0 20 20"><use href="#star" fill="#f5a800"/></svg><svg viewBox="0 0 20 20"><use href="#star" fill="#f5a800"/></svg><svg viewBox="0 0 20 20"><use href="#star" fill="#f5a800"/></svg><svg viewBox="0 0 20 20"><use href="#star" fill="#f5a800"/></svg><svg viewBox="0 0 20 20"><use href="#star" fill="url(#half)" stroke="#f5a800" stroke-width="1.3"/></svg></div><span>(123)</span></div>
      <svg class="fav" viewBox="0 0 20 19"><use href="#heart" fill="none" stroke="#555" stroke-width="1.6"/></svg>
    </article>
  </div>
</main>

<svg class="loader" viewBox="-55 -55 110 110" aria-label="Loading">
  <g stroke-linecap="round" stroke-width="9">
    <line x1="0" y1="-28" x2="0" y2="-48" stroke="#bdbdbd"/>
    <line x1="0" y1="-28" x2="0" y2="-48" stroke="#ececec" transform="rotate(30)"/>
    <line x1="0" y1="-28" x2="0" y2="-48" stroke="#ececec" transform="rotate(60)"/>
    <line x1="0" y1="-28" x2="0" y2="-48" stroke="#e6e6e6" transform="rotate(90)"/>
    <line x1="0" y1="-28" x2="0" y2="-48" stroke="#e0e0e0" transform="rotate(120)"/>
    <line x1="0" y1="-28" x2="0" y2="-48" stroke="#d9d9d9" transform="rotate(150)"/>
    <line x1="0" y1="-28" x2="0" y2="-48" stroke="#d3d3d3" transform="rotate(180)"/>
    <line x1="0" y1="-28" x2="0" y2="-48" stroke="#cdcdcd" transform="rotate(210)"/>
    <line x1="0" y1="-28" x2="0" y2="-48" stroke="#c8c8c8" transform="rotate(240)"/>
    <line x1="0" y1="-28" x2="0" y2="-48" stroke="#c4c4c4" transform="rotate(270)"/>
    <line x1="0" y1="-28" x2="0" y2="-48" stroke="#c0c0c0" transform="rotate(300)"/>
    <line x1="0" y1="-28" x2="0" y2="-48" stroke="#bdbdbd" transform="rotate(330)"/>
  </g>
</svg>

<footer class="site-footer">
  <p>Copyright © 2015.www.Clinora .All Rights Reserved</p>
  <nav class="social">
    <a><i></i>ruvanteo</a>
    <a><i></i>plombex</a>
    <a><i></i>melvoshade</a>
  </nav>
</footer>
</body>
</html>
```